New Corporate Business Card - Velmorabelle

What we need:
We need a new corporate business card.
We want a new template that we can change by ourself.
We want business card modern and minimalist but that looks professional.
We will print it in 300 gr soft-touch.
Why not a white side with the logo and a red/grey side with the content?
Why not a grey side and a red side like our logo?
I am sure that you have better idea than ours that's the reason we come here.

Who we are:
We are a private label company in cosmetics based in Switzerland. We work in BtoB. We make skin care products for other brands.

Target Market(s)

B to B - Worldwide - any gender

Industry/Entity Type

Cosmetics

Contact Information for Business Card

Side 1:
Logo
Your Swiss Private Label Manufacturer or www.velmorabelle.ch

Side 2:
Name and surname (Example: Lucien Marchetaz)
Job Description (General Manager)
Telephone (+41 32 918 64 00)
Direct (+41 32 918 64 64)
Email (lucien.marchetaz@velmorabelle.ch)
Chemin des Prés-Fleuris 14, 2000 Neuchâtel, Switzerland
www.velmorabelle.ch

Font styles to use
Serif
Sans Serif

Requirements
Must have
• You can use 4 colors: white, red, grey and/or black .
Should not have
• Too much colors, too much things. We want it simple!

```html
<!DOCTYPE html>
<html lang="en">
<head>
<meta charset="utf-8">
<title>Velmorabelle – Business Card</title>
<link rel="stylesheet" href="https://fonts.googleapis.com/css2?family=Nunito:wght@800&family=Questrial&display=swap">
<style>
  :root {
    --red: #e31b36;
    --red-soft: #e8334b;
    --grey: #b3b3b3;
    --grey-light: #c4c4c4;
    --text-grey: #6d6d6d;
    --ink: #5a5a5a;
    --white: #ffffff;
    --backdrop: #ecebe8;
    --rule: #cfcfcf;
  }
  * { box-sizing: border-box; margin: 0; padding: 0; }
  html, body {
    width: 1200px; height: 960px; overflow: hidden;
    background: var(--backdrop);
    font-family: "Questrial", "Century Gothic", sans-serif;
  }
  .canvas { position: relative; width: 1200px; height: 960px; }

  .card {
    position: absolute; left: 232px; width: 736px; height: 420px;
    box-shadow: 0 6px 18px rgba(0,0,0,.14);
    overflow: hidden;
  }

  /* Side 1 – brand side */
  .card--brand { top: 40px; background: var(--red); }
  .card--brand .pattern-fill {
    position: absolute; inset: 0;
    background: linear-gradient(135deg, var(--red) 0%, var(--red-soft) 100%);
  }
  .card--brand .brand-name {
    position: absolute; inset: 0;
    display: flex; align-items: center; justify-content: center;
    color: var(--white); font-size: 58px; letter-spacing: 6px;
  }

  /* Side 2 – contact side */
  .card--contact { top: 500px; background: var(--white); }
  .contact-logo {
    position: absolute; left: 40px; top: 80px; width: 352px; height: 200px;
    display: flex; align-items: center; justify-content: center; gap: 14px;
    color: var(--red); font-size: 40px; letter-spacing: 3px;
  }
  .contact-logo .mark { width: 20px; height: 20px; background: var(--red); }
  .divider {
    position: absolute; left: 440px; top: 92px; width: 1px; height: 200px;
    background: var(--rule);
  }
  .details { position: absolute; left: 470px; top: 104px; width: 250px; color: var(--text-grey); }
  .person-name {
    font-family: "Nunito", "Century Gothic", sans-serif; font-weight: 800;
    font-size: 25px; color: var(--ink); line-height: 1.05;
  }
  .person-role { font-size: 14px; margin-top: 2px; }
  .address { font-size: 14px; line-height: 1.35; margin-top: 16px; }
  .contact-list { list-style: none; margin-top: 12px; font-size: 15px; }
  .contact-list li { display: flex; align-items: center; gap: 12px; height: 24px; }
  .contact-list svg { width: 15px; height: 15px; flex: none; }
  .footer-band {
    position: absolute; left: 0; right: 0; bottom: 0; height: 62px;
    background: var(--grey-light);
  }
</style>
</head>
<body>
<main class="canvas">

  <section class="card card--brand" aria-label="Business card front">
    <div class="pattern-fill" role="img" aria-label="Red background with a fine white dotted grid pattern"></div>
    <div class="brand-name">Velmorabelle</div>
  </section>

  <section class="card card--contact" aria-label="Business card back">
    <div class="contact-logo"><span class="mark"></span><span>Velmorabelle</span></div>
    <div class="divider"></div>

    <div class="details">
      <p class="person-name">Lucien Marchetaz</p>
      <p class="person-role">Managing Partner</p>
      <p class="address">Chemin des Prés-Fleuris 14,<br>2000 Neuchâtel, Switzerland</p>
      <ul class="contact-list">
        <li>
          <svg viewBox="0 0 16 16" aria-hidden="true"><path fill="var(--red)" d="M3.5 1.5l2.5-.5 1.5 3.5-1.8 1.2a8 8 0 0 0 4.6 4.6l1.2-1.8 3.5 1.5-.5 2.5c-.2.8-1 1.3-1.8 1.2C6.8 13 3 9.2 2.3 3.3c-.1-.8.4-1.6 1.2-1.8z"/></svg>
          000 000 0000
        </li>
        <li>
          <svg viewBox="0 0 16 16" aria-hidden="true"><g fill="var(--red)"><rect x="4" y="1" width="8" height="4"/><rect x="1" y="6" width="14" height="6" rx="1"/><rect x="4" y="10" width="8" height="5" fill="var(--white)" stroke="var(--red)" stroke-width="1.2"/></g></svg>
          000 000 0000
        </li>
        <li>
          <svg viewBox="0 0 16 16" aria-hidden="true"><g fill="none" stroke="var(--red)" stroke-width="1.3"><rect x="1" y="3" width="14" height="10"/><path d="M1 3l7 6 7-6"/></g></svg>
          info@velmorabelle.ch
        </li>
        <li>
          <svg viewBox="0 0 16 16" aria-hidden="true"><g fill="none" stroke="var(--red)" stroke-width="1.2"><circle cx="8" cy="8" r="6.5"/><ellipse cx="8" cy="8" rx="3" ry="6.5"/><path d="M1.5 8h13M2.5 4.7h11M2.5 11.3h11"/></g></svg>
          www.velmorabelle.ch
        </li>
      </ul>
    </div>

    <div class="footer-band" role="img" aria-label="Grey band with a fine white dotted diagonal grid pattern"></div>
  </section>

</main>
</body>
</html>
```